hotel's Website

Hotels website redesign for reference pictures, logo etc see http://restwellmarlow.co.uk/

1. 2-3 Special offers on the main page.
2. Booking calender
3. Location Map
4. Picture gallery.
5. Journeyscope reviews.
6. short description
7. Social Media sharing.
8 Phone number and address.

Industry/Entity Type

Hotel

Requirements
Must have
• 1. 2-3 Special offers on the main page.
2. Booking calender
3. Location Map
4. Picture gallery.
5. Journeyscope reviews.
6. short description
7. Social Media sharing.

```html
<!DOCTYPE html>
<html lang="en">
<head>
<meta charset="utf-8">
<title>City hotel</title>
<link href="https://fonts.googleapis.com/css2?family=Marcellus&family=Lato:wght@400;700&display=swap" rel="stylesheet">
<style>
:root{
  --dark:#1e130f;
  --darker:#120b08;
  --bar:#241612;
  --gold:#c9a24a;
  --orange:#f0a020;
  --accent:#b05a18;
  --paper:#f1ebe1;
  --ink:#3a2a22;
  --line:#8a5a30;
  --muted:#6d625b;
}
*{margin:0;padding:0;box-sizing:border-box}
html,body{width:772px;height:1200px;overflow:hidden}
body{position:relative;background:var(--paper);font-family:"Marcellus",Georgia,serif;color:var(--ink)}
.abs{position:absolute}
.hero{left:0;top:0;width:772px;height:355px;background:radial-gradient(ellipse at 50% 60%,#d2a66a 0%,#8a5a32 30%,#4a2e1a 65%,#24170e 100%)}
.topbar{left:0;top:0;width:772px;height:62px;background:rgba(30,20,14,.72)}
.logo{left:124px;top:16px;font-size:27px;color:#fff}
.nav{top:33px;font-size:9.5px;color:#fff}
.nav.active{color:var(--orange)}
.nav-sep{top:28px;width:1px;height:20px;background:rgba(255,255,255,.25)}
.arrow{top:196px;width:24px;height:24px;background:rgba(255,255,255,.35)}
.search{left:0;top:355px;width:772px;height:37px;background:var(--bar);border-bottom:3px solid var(--gold)}
.search-label{left:117px;top:367px;font-size:11px;color:#fff}
.field{top:365px;width:96px;height:18px;background:#fff;font-size:8.5px;color:#aaa;padding:3px 5px}
.field i{position:absolute;right:4px;top:5px;width:8px;height:8px;background:#555}
.submit{left:607px;top:365px;width:58px;height:18px;background:var(--gold);color:#fff;font-size:8.5px;text-align:center;line-height:18px}
h2{position:absolute;font-weight:400;font-size:12.5px;color:var(--ink)}
h2 span{display:inline-block;width:46px;height:1px;background:var(--ink);vertical-align:middle;margin-left:8px}
.photo{border:3px solid #fff;box-shadow:0 0 2px rgba(0,0,0,.3)}
.badge{width:38px;height:18px;background:var(--gold);color:#fff;font-size:8px;line-height:18px;text-align:center}
.card-title{font-size:10px;color:var(--ink)}
.price{font-size:10px;color:var(--ink)}
.card-text{width:172px;font-size:7px;line-height:9.4px;color:var(--accent)}
.more{font-size:7.5px;color:var(--ink)}
.divider{left:116px;width:549px;height:1px;background:var(--line)}
.intro{left:116px;top:682px;width:351px;height:131px;background:var(--dark)}
.intro-title{left:286px;top:693px;font-size:12px;color:#fff}
.intro-text{left:286px;top:713px;width:175px;font-size:8.3px;line-height:9.3px;color:#eee}
.footer{left:0;top:1018px;width:772px;height:152px;background:var(--darker)}
.copy-bar{left:0;top:1170px;width:772px;height:30px;background:#1c120e}
.f-head{font-size:9.5px;color:#fff}
.f-text{font-family:"Lato",Arial,sans-serif;font-size:7px;line-height:9.5px}
.social{top:1178px;width:14px;height:14px;border-radius:50%;background:#5b514c}
</style>
</head>
<body>
<div class="abs hero" role="img" aria-label="Photo of a candle-lit dining table on a poolside terrace at night"></div>
<div class="abs topbar"></div>
<div class="abs logo">City hotel</div>
<div class="abs nav active" style="left:385px">Home</div>
<div class="abs nav-sep" style="left:420px"></div>
<div class="abs nav" style="left:431px">About us</div>
<div class="abs nav-sep" style="left:475px"></div>
<div class="abs nav" style="left:486px">Service</div>
<div class="abs nav-sep" style="left:523px"></div>
<div class="abs nav" style="left:535px">Rooms</div>
<div class="abs nav-sep" style="left:571px"></div>
<div class="abs nav" style="left:582px">Blog</div>
<div class="abs nav-sep" style="left:610px"></div>
<div class="abs nav" style="left:621px">Contact us</div>
<svg class="abs arrow" style="left:28px" viewBox="0 0 24 24"><path d="M14 6 L9 12 L14 18" stroke="#fff" fill="none"/></svg>
<svg class="abs arrow" style="left:717px" viewBox="0 0 24 24"><path d="M10 6 L15 12 L10 18" stroke="#fff" fill="none"/></svg>

<div class="abs search"></div>
<div class="abs search-label">SERCH ROOM</div>
<div class="abs field" style="left:196px">Check in<i></i></div>
<div class="abs field" style="left:298px">Check Out<i></i></div>
<div class="abs field" style="left:401px">Adults<i></i></div>
<div class="abs field" style="left:504px">Children<i></i></div>
<div class="abs submit">Submit</div>

<h2 style="left:116px;top:415px">Special Offers<span></span></h2>

<div class="abs photo" style="left:116px;top:437px;width:172px;height:96px;background:linear-gradient(135deg,#7a6a5a,#3a2a20)" role="img" aria-label="Standard room with bed and flowers"></div>
<div class="abs badge" style="left:254px;top:510px">10% OFF</div>
<div class="abs card-title" style="left:117px;top:538px">Standard Room</div>
<div class="abs price" style="left:258px;top:538px">$120.00</div>
<div class="abs card-text" style="left:117px;top:552px">Lorem ipsum dolor sit amet, consectetur adipisicing elit, sed do eiusmod tempor incididunt ut labore et dolore magna aliqua.</div>
<div class="abs more" style="left:117px;top:585px">Read More</div>

<div class="abs photo" style="left:305px;top:437px;width:172px;height:96px;background:linear-gradient(135deg,#b8a58a,#4a3a30)" role="img" aria-label="Double room with two beds"></div>
<div class="abs badge" style="left:443px;top:510px">25% OFF</div>
<div class="abs card-title" style="left:306px;top:538px">Double Room</div>
<div class="abs price" style="left:447px;top:538px">$160.00</div>
<div class="abs card-text" style="left:306px;top:552px">Lorem ipsum dolor sit amet, consectetur adipisicing elit, sed do eiusmod tempor incididunt ut labore et dolore magna aliqua.</div>
<div class="abs more" style="left:306px;top:585px">Read More</div>

<div class="abs photo" style="left:494px;top:437px;width:172px;height:96px;background:linear-gradient(135deg,#d8a050,#6a4020)" role="img" aria-label="King suite lounge with sofas"></div>
<div class="abs badge" style="left:632px;top:510px">20% OFF</div>
<div class="abs card-title" style="left:495px;top:538px">King Suit</div>
<div class="abs price" style="left:636px;top:538px">$200.00</div>
<div class="abs card-text" style="left:495px;top:552px">Lorem ipsum dolor sit amet, consectetur adipisicing elit, sed do eiusmod tempor incididunt ut labore et dolore magna aliqua.</div>
<div class="abs more" style="left:495px;top:585px">Read More</div>

<div class="abs divider" style="top:630px"></div>

<h2 style="left:116px;top:659px">City Hotel<span></span></h2>
<h2 style="left:487px;top:659px">Location Map<span></span></h2>
<div class="abs intro"></div>
<div class="abs photo" style="left:128px;top:693px;width:148px;height:108px;background:linear-gradient(135deg,#c07840,#5a2a10)" role="img" aria-label="Hotel lounge with leather sofa"></div>
<div class="abs intro-title">Lorem ipsum dolor sit amet</div>
<div class="abs intro-text">Lorem ipsum dolor sit amet, consectetur adipisicing elit, sed do eiusmod tempor incididunt ut labore et dolore magna aliqua. Ut enim ad minim veniam, quis nostrud exercitation ullamco laboris nisi ut aliquip ex ea commodo consequat. Duis aute irure dolor in reprehenderit in voluptate velit esse cillum dolore eu fugiat nulla pariatur.</div>
<div class="abs" style="left:286px;top:792px;font-size:8.5px;color:#fff">Read More <span style="color:var(--orange)">→</span></div>
<div class="abs photo" style="left:487px;top:682px;width:178px;height:130px;background:linear-gradient(135deg,#e6e2d6,#d6dccf 50%,#a9c7ea)" role="img" aria-label="Location map of the hotel region"></div>

<div class="abs divider" style="top:845px"></div>

<h2 style="left:116px;top:870px">Hotel Gallery<span></span></h2>
<div class="abs photo" style="left:117px;top:892px;width:130px;height:87px;background:linear-gradient(135deg,#c08030,#3a1a08)" role="img" aria-label="Concierge desk"></div>
<div class="abs photo" style="left:256px;top:892px;width:130px;height:87px;background:#6a4a35" role="img" aria-label="Hotel hall"></div>
<svg class="abs" style="left:308px;top:923px" width="26" height="26" viewBox="0 0 26 26"><circle cx="13" cy="13" r="12" fill="#d8d0c8" opacity=".85"/><path d="M13 7v12M7 13h12" stroke="#6a4a35" stroke-width="3"/></svg>
<div class="abs photo" style="left:395px;top:892px;width:130px;height:87px;background:linear-gradient(135deg,#b09070,#3a2a20)" role="img" aria-label="Twin bedroom"></div>
<div class="abs photo" style="left:534px;top:892px;width:131px;height:87px;background:linear-gradient(135deg,#e0b860,#7a3a18)" role="img" aria-label="Bed with decorative pillows"></div>

<div class="abs footer"></div>
<div class="abs f-head" style="left:117px;top:1030px">About Us</div>
<div class="abs f-text" style="left:119px;top:1052px;width:160px;color:#fff;font-size:7.5px">Duis fringilla erat nec aliquet tincidunt. Fusce posuere erat vitae nibh rutrum sagittis. Morbi dignissim.</div>
<div class="abs f-text" style="left:119px;top:1088px;width:170px;color:#6d625b">Lorem ipsum dolor sit amet, consectetur adipisicing elit. Sed ac urna in erat commodo euismod. Nullam ac luctus turpis.</div>
<div class="abs" style="left:119px;top:1127px;font-size:8px;color:#fff">Read More <span style="color:var(--orange)">→</span></div>

<div class="abs f-head" style="left:325px;top:1027px">Latest news</div>
<div class="abs f-text" style="left:325px;top:1049px;width:160px;color:#fff"><span style="color:var(--orange)">22.06.2013</span> consectetur adipiscing elit.</div>
<div class="abs f-text" style="left:325px;top:1059px;width:150px;color:#4e433d">Sed ac urna in erat commodo euismod. Nullam ac luctus turpis porta.</div>
<div class="abs" style="left:325px;top:1086px;width:163px;height:1px;background:#2e2420"></div>
<div class="abs f-text" style="left:325px;top:1095px;width:160px;color:#fff"><span style="color:var(--orange)">22.06.2013</span> consectetur adipiscing elit.</div>
<div class="abs f-text" style="left:325px;top:1105px;width:150px;color:#4e433d">Sed ac urna in erat commodo euismod. Nullam ac luctus turpis porta.</div>

<div class="abs f-head" style="left:545px;top:1027px">Contact Us</div>
<svg class="abs" style="left:530px;top:1048px" width="8" height="11" viewBox="0 0 8 11"><path d="M4 0a4 4 0 0 0-4 4c0 3 4 7 4 7s4-4 4-7a4 4 0 0 0-4-4z" fill="#fff"/><circle cx="4" cy="4" r="1.5" fill="#120b08"/></svg>
<div class="abs f-text" style="left:546px;top:1047px;color:#fff;line-height:14px">No 12 Harbor Lane 45/1 New York<br>City , NY United States</div>
<svg class="abs" style="left:529px;top:1078px" width="10" height="8" viewBox="0 0 10 8"><rect width="10" height="8" fill="#fff"/><path d="M0 0 L5 4 L10 0" stroke="#120b08" fill="none"/></svg>
<div class="abs f-text" style="left:546px;top:1076px;color:#fff;line-height:14px">stay@cityhotelrooms.com<br>stay@cityhotelrooms.com</div>
<svg class="abs" style="left:529px;top:1107px" width="10" height="8" viewBox="0 0 10 8"><path d="M0 3 Q5 -1 10 3 L9 4 L7 3 L3 3 L1 4Z M2 4 H8 V8 H2Z" fill="#fff"/></svg>
<div class="abs f-text" style="left:546px;top:1105px;color:#fff;line-height:14px">(+40) 04401020304<br>(+40) 04401020304</div>
<svg class="abs" style="left:529px;top:1142px" width="12" height="12"><circle cx="6" cy="6" r="6" fill="#fff"/></svg>
<div class="abs" style="left:545px;top:1139px;font-family:'Lato',Arial,sans-serif;font-size:14px;font-weight:700;color:#fff">Journeyscope</div>

<div class="abs copy-bar"></div>
<div class="abs f-text" style="left:117px;top:1180px;color:#6d625b">Copyright ©2013 City hotel. All Rights Reserved.</div>
<div class="abs social" style="left:580px"></div>
<div class="abs social" style="left:598px"></div>
<div class="abs social" style="left:616px"></div>
<div class="abs social" style="left:634px"></div>
<div class="abs social" style="left:652px"></div>
</body>
</html>
```